Music Festival Business Cards

The Lantern Gathering
Produced by Bramblewood Sound Collective LLC
New music festival in Arkansas.

Target Market(s)

18-35 year olds

Industry/Entity Type

Festival

Contact Information for Business Card

We are a 5-partner team producing a music festival in Arkansas. We need slick business cards, and I want them to be square.

Requirements
Must have
• I NEED THESE TO BE IN SQUARE SIZE - 2x2 or 2.5x2.5... please not regular size.
• I need www.lanternmeet.example as the link to website.

```html
<!DOCTYPE html>
<html lang="en">
<head>
<meta charset="utf-8">
<title>The Lantern Gathering – Square Business Cards</title>
<link href="https://fonts.googleapis.com/css2?family=Orbitron:wght@500;700;800&family=Exo+2:wght@400;500&display=swap" rel="stylesheet">
<style>
  :root {
    --backdrop: #1c1c1e;
    --card: #0d0d0e;
    --card-edge: #161617;
    --teal: #3fc4cc;
    --white: #f2f2f2;
    --silver: #b9bcbf;
  }
  * { box-sizing: border-box; margin: 0; padding: 0; }
  html, body { width: 1200px; height: 1200px; overflow: hidden; }
  body {
    background: var(--backdrop);
    font-family: "Exo 2", "Trebuchet MS", sans-serif;
    position: relative;
  }
  .card {
    position: absolute;
    top: 330px;
    width: 540px;
    height: 540px;
    background: linear-gradient(135deg, #111112 0%, var(--card) 60%, #0a0a0b 100%);
    border: 1px solid var(--card-edge);
    box-shadow: 0 18px 40px rgba(0,0,0,0.55);
  }
  .card--front { left: 40px; }
  .card--back { left: 620px; }

  /* Front */
  .front-brand {
    position: absolute;
    left: 0; right: 0; top: 120px;
    text-align: center;
  }
  .brand-dot {
    width: 76px; height: 76px;
    margin: 0 auto 34px;
    border: 7px solid var(--teal);
    border-radius: 50%;
  }
  .brand-name {
    font-family: "Orbitron", sans-serif;
    font-weight: 800;
    font-size: 40px;
    line-height: 1.15;
    letter-spacing: 3px;
    color: var(--teal);
    text-transform: uppercase;
  }
  .brand-producer {
    margin-top: 16px;
    font-family: "Orbitron", sans-serif;
    font-weight: 500;
    font-size: 12px;
    line-height: 1.7;
    letter-spacing: 2px;
    color: var(--teal);
    text-transform: uppercase;
  }

  /* Back */
  .person { position: absolute; left: 40px; top: 44px; }
  .person-name {
    font-family: "Orbitron", sans-serif;
    font-weight: 700;
    font-size: 32px;
    letter-spacing: 3px;
    color: var(--white);
    text-transform: uppercase;
  }
  .person-role {
    margin-top: 6px;
    font-family: "Orbitron", sans-serif;
    font-weight: 500;
    font-size: 13px;
    letter-spacing: 5px;
    color: var(--teal);
    text-transform: uppercase;
  }
  .back-mark {
    position: absolute;
    right: 40px; top: 150px;
    font-family: "Orbitron", sans-serif;
    font-weight: 700;
    font-size: 18px;
    line-height: 1.4;
    letter-spacing: 3px;
    color: var(--silver);
    text-align: right;
    text-transform: uppercase;
  }
  .divider {
    position: absolute;
    left: 40px; right: 40px; top: 250px;
    height: 3px;
    background: var(--teal);
  }
  .contact-list {
    position: absolute;
    left: 40px; top: 272px;
    list-style: none;
  }
  .contact-list li, .address {
    display: flex;
    align-items: center;
    gap: 14px;
    font-size: 17px;
    letter-spacing: 1px;
    color: var(--white);
    line-height: 36px;
  }
  .icon { width: 22px; height: 22px; fill: var(--teal); flex: none; }
  .address {
    position: absolute;
    left: 40px; top: 430px;
    align-items: flex-start;
    line-height: 30px;
  }
  .address .icon { margin-top: 4px; }
</style>
</head>
<body>

  <section class="card card--front" aria-label="Card front">
    <div class="front-brand">
      <div class="brand-dot"></div>
      <h1 class="brand-name">The Lantern<br>Gathering</h1>
      <p class="brand-producer">Produced by<br>Bramblewood Sound Collective LLC</p>
    </div>
  </section>

  <section class="card card--back" aria-label="Card back">
    <div class="person">
      <h2 class="person-name">Marcus Hale</h2>
      <p class="person-role">Managing Director</p>
    </div>

    <p class="back-mark">The Lantern<br>Gathering</p>

    <div class="divider"></div>

    <ul class="contact-list">
      <li>
        <svg class="icon" viewBox="0 0 24 24" aria-hidden="true"><path d="M6.6 10.8a15.1 15.1 0 0 0 6.6 6.6l2.2-2.2a1 1 0 0 1 1-.25 11.4 11.4 0 0 0 3.6.57 1 1 0 0 1 1 1V20a1 1 0 0 1-1 1A17 17 0 0 1 3 4a1 1 0 0 1 1-1h3.5a1 1 0 0 1 1 1c0 1.25.2 2.45.57 3.57a1 1 0 0 1-.25 1z"/></svg>
        501 555 0147
      </li>
      <li>
        <svg class="icon" viewBox="0 0 24 24" aria-hidden="true"><path d="M7 3h10v4H7zM4 8h16a2 2 0 0 1 2 2v6h-4v5H6v-5H2v-6a2 2 0 0 1 2-2zm4 8v3h8v-3z"/></svg>
        501 555 0148
      </li>
      <li>
        <svg class="icon" viewBox="0 0 24 24" aria-hidden="true"><path d="M2 5h20v14H2zm2 2v.5l8 5.5 8-5.5V7l-8 5.5z"/></svg>
        marcus@lanternmeet.example
      </li>
      <li>
        <svg class="icon" viewBox="0 0 24 24" aria-hidden="true"><path d="M12 2a10 10 0 1 0 0 20 10 10 0 0 0 0-20zm6.9 6h-2.9a15.6 15.6 0 0 0-1.4-3.6A8 8 0 0 1 18.9 8zM12 4c.8 1.2 1.5 2.5 1.9 4h-3.8c.4-1.5 1.1-2.8 1.9-4zM4.3 14a8 8 0 0 1 0-4h3.4a16.5 16.5 0 0 0 0 4zm.8 2h2.9c.3 1.3.8 2.5 1.4 3.6A8 8 0 0 1 5.1 16zM8 8H5.1a8 8 0 0 1 4.3-3.6C8.8 5.5 8.3 6.7 8 8zm4 12c-.8-1.2-1.5-2.5-1.9-4h3.8c-.4 1.5-1.1 2.8-1.9 4zm2.3-6H9.7a14.7 14.7 0 0 1 0-4h4.6a14.7 14.7 0 0 1 0 4zm.3 5.6c.6-1.1 1.1-2.3 1.4-3.6h2.9a8 8 0 0 1-4.3 3.6zm1.7-5.6a16.5 16.5 0 0 0 0-4h3.4a8 8 0 0 1 0 4z"/></svg>
        www.lanternmeet.example
      </li>
    </ul>

    <div class="address">
      <svg class="icon" viewBox="0 0 24 24" aria-hidden="true"><path d="M12 2a7 7 0 0 0-7 7c0 5.2 7 13 7 13s7-7.8 7-13a7 7 0 0 0-7-7zm0 9.5A2.5 2.5 0 1 1 12 6.5a2.5 2.5 0 0 1 0 5z"/></svg>
      <span>14 Orchard Lane<br>Suite 208, Harlow AR 72001</span>
    </div>
  </section>

</body>
</html>
```